Design eines Zertifikats
Ich bin total begeistert. Super Kommunikation, super schnelle Reaktion auf kleine Änderungswünsche, ich bin wirklich rundum zufrieden!! Auch bei weiterführenden Fragen die gar nicht direkt mit dem Design zusammenhingen wurde mir total schnell und sympathisch geholfen, ich kann die Designerin nur wärmstens weiterempfehlen!
Zielgruppe
Ich betreibe einen Onlineshop, in dem ich sogenannte Sterntaufen verkaufe. Ein Kunde bekommt dabei im Zuge seines Kaufes ein Zertifikat ausgestellt mit Daten zu seinem getauften Stern. Es geht hier um das Design eines neuen Zertifikats um möglichst noch mehr Käufer anzusprechen. Es sind bereits 3 Designs vorhanden, das neue sollte sich entsprechend etwas absetzen.
Ich lasse die Zertifikate in einer Druckerei drucken, und bedrucke diese dann selber mit den Daten der Sterntaufe, es muss auf dem Zertifikat also ein heller Bereich vorhanden sein in dem ich drucken kann.
Aufgabenstellung
Das Zertifikat soll A4 sein. Es sollte modern sein und sich wie gesagt möglichst von den bestehenden absetzen, und ein möglichst breites Publikum ansprechen.
Beispiele für Zertifikate der Konkurrenz finden sich unter:
lichtpunkt-shop.de
nebelbuchung.de
himmelsgabe-online.de
Das von lichtpunkt-shop.de gefällt mir persönlich ganz gut, aber lasst euch nicht von den Vorschlägen einschränken.
Bitte nicht zu exzessiv kostenpflichtiges Stockmaterial verwenden, ich mache leider aktuell noch Miese mit dem Shop :-)
Bitte schaut auf meine Webseite um ein Gefühl dafür zu bekommen wie viel Platz für Text vorhanden sein muss.

```html
<!DOCTYPE html>
<html lang="de">
<head>
<meta charset="utf-8">
<title>Sternurkunde</title>
<link href="https://fonts.googleapis.com/css2?family=Playfair+Display:wght@400;700&display=swap" rel="stylesheet">
<style>
  :root {
    --paper: #fbfbfc;
    --paper-shade: #e6e7ea;
    --ink: #111114;
    --navy: #24306f;
    --gold-light: #f0d58c;
    --gold-dark: #a67a2c;
    --space-deep: #1b1742;
    --space-mid: #3a2f7a;
    --space-glow: #6e4f8f;
  }
  * { margin: 0; padding: 0; box-sizing: border-box; }
  html, body { width: 1200px; height: 849px; overflow: hidden; background: var(--paper); }
  .certificate {
    position: relative;
    width: 1200px;
    height: 849px;
    overflow: hidden;
    font-family: "Playfair Display", Georgia, serif;
    color: var(--ink);
    background:
      radial-gradient(ellipse 70% 30% at 75% 5%, var(--paper-shade), transparent 70%),
      radial-gradient(ellipse 60% 25% at 20% 62%, #eceef1, transparent 70%),
      var(--paper);
  }
  .decor { position: absolute; inset: 0; width: 1200px; height: 849px; }
  .seal { position: absolute; left: 958px; top: 93px; width: 154px; height: 154px; }
  .title {
    position: absolute; left: 106px; top: 84px;
    font-size: 86px; font-weight: 400; letter-spacing: 0.5px; line-height: 1;
  }
  .lead {
    position: absolute; left: 104px;
    font-size: 22px; font-weight: 700;
  }
  .lead--data { top: 238px; }
  .lead--name { top: 426px; }
  .data {
    position: absolute; left: 104px;
    font-size: 18.5px; line-height: 27px;
    display: grid; grid-template-columns: 219px auto;
  }
  .data--star { top: 294px; }
  .data--baptism { top: 552px; }
  .star-name {
    position: absolute; left: 104px; top: 480px;
    font-size: 38px; font-weight: 700; letter-spacing: 4px;
  }
</style>
</head>
<body>
<main class="certificate">
  <svg class="decor" viewBox="0 0 842 596" preserveAspectRatio="none" aria-hidden="false">
    <defs>
      <linearGradient id="gold" x1="0" y1="0" x2="1" y2="0">
        <stop offset="0" stop-color="var(--gold-light)"/>
        <stop offset="0.5" stop-color="var(--gold-dark)"/>
        <stop offset="1" stop-color="var(--gold-light)"/>
      </linearGradient>
      <linearGradient id="gold-right" x1="0" y1="0" x2="1" y2="0">
        <stop offset="0" stop-color="var(--gold-dark)"/>
        <stop offset="0.6" stop-color="var(--gold-light)"/>
        <stop offset="1" stop-color="var(--gold-dark)"/>
      </linearGradient>
      <linearGradient id="space" x1="0" y1="0" x2="1" y2="1">
        <stop offset="0" stop-color="var(--space-deep)"/>
        <stop offset="0.45" stop-color="var(--space-mid)"/>
        <stop offset="0.7" stop-color="var(--space-glow)"/>
        <stop offset="1" stop-color="var(--space-deep)"/>
      </linearGradient>
    </defs>
    <path class="night-sky" role="img" aria-label="Sternenhimmel mit Milchstraße"
          fill="url(#space)"
          d="M0,498 C150,505 300,482 450,452 C600,422 720,404 842,410 L842,596 L0,596 Z"/>
    <path class="swoosh swoosh--left" fill="url(#gold)"
          d="M0,434 C80,468 200,480 300,466 C360,458 410,450 442,443 C400,456 330,472 260,480 C160,492 60,480 0,462 Z"/>
    <path class="swoosh swoosh--right" fill="url(#gold-right)"
          d="M400,494 C500,468 620,440 720,436 C792,434 830,470 842,512 L842,442 C800,420 740,418 680,425 C580,436 480,464 400,494 Z"/>
  </svg>

  <svg class="seal" viewBox="0 0 108 108" aria-hidden="true">
    <circle cx="54" cy="54" r="52" fill="var(--navy)"/>
    <circle cx="54" cy="54" r="44" fill="var(--paper)"/>
  </svg>

  <h1 class="title">Sternurkunde</h1>

  <p class="lead lead--data">Der Stern mit den Daten</p>
  <dl class="data data--star">
    <dt>HIP-No.</dt><dd>11767</dd>
    <dt>Rektamension</dt><dd>02h 31m 47.08s</dd>
    <dt>Deklination</dt><dd>+89° 15' 50.9'</dd>
    <dt>Scheinbare Magnitude</dt><dd>1,97</dd>
  </dl>

  <p class="lead lead--name">wurde auf der Namen getauft</p>
  <p class="star-name">Maria</p>

  <dl class="data data--baptism">
    <dt>Taufdatum</dt><dd>14.02.2020</dd>
    <dt>Registrationsnummer</dt><dd>xxx-xxx-xxx-xxx</dd>
  </dl>
</main>
</body>
</html>
```